What's Needed:
- All designs files created
- Fully coded implementation in HTML/CSS/Bootstrap
- Pages: 5 -- see content here http://www.TeamPrismly.com
-- Home Page
-- The Hidden Value
-- Benefits
-- About us
-- Careers
- The existing site has the textual content for each page. We can tweak to meet specific designs if needed.
- You will need to update/create image and interactive content for pages.

Reference:
Our existing website has a lot of content on it for reference -
http://www.TeamPrismly.com

Description:
We need a web design that focuses in the UX and conveys the idea of magically fixing company problems by way of using our software.

Home Page
The main goal is to Drive Sales of the SaaS tool. When a visitor lands on our home page they should see: What we do, How we can help their problem and How to contact us.
1. Quickly understand What We Do
-- we sell SaaS software.
-- Need to quickly convey what our software does. It's seems complicated but really its not. See the description in about us for more info and visit our existing site.

2. How we can help their problem
-- We aim to solve any problem related to employees
-- Even if the visitor does not have a specific problem in mind, there are several areas organizations can always improve: (some examples below)
---- Create Stronger, More Productive Teams
---- Build Better Communications Pathways
---- Encourage Innovation and Positive Change
---- Develop and Retain Strong "Company Culture"

3. Be able to Contact Us to get started
-- contacting us to get a sales lead is the ultimate goal.
-- the user should not have to hunt to contact us. needs to be easy.

Other Pages (Hidden Value, Benefit, About Us, Careers):
-- These are informative pages about our software and process.
-- If we grab the attention of the user on the home page then these are the pages that they will explore for more info.
-- Should be able to link to these pages from the main nav or from sections with the homepage. For example: What We Do sections could link to the benefits page. How we help their problem sections could link to the Hidden Value page. Regardless of what links to where, the idea is that we will be able to nav to other areas.

About Us:
Our company name is TeamPrismly (as in Organizational Analysis). We provide a software as a service (SaaS) that uses a simple 6-question survey to analyze the relationships of people within an Organization and provide leaders with ground-breaking Insights about their teams, interactive social network data visualizations to explore their team's composition and we give detailed profiles of the key players (i.e, who are the Social Bridges, Who are the Knowledge Bottlenecks, Who are the Best Mentors, Who are the people that are completely disconnected/out of the loop). Leaders then use this information to make high level organizational decisions.

What's unique about our software:
-- Powerful analysis results from just a 6-question "pulse-surveys"
-- Innovative Tools for visually exploring the organization through relationships as opposed to org-chart
-- Get real-time results as opposed to waiting months with traditional methods
-- Traditional Org-charts represent the organization's skeleton, whereas we uncover the organization's neural network (how it solves problems).

Preferred fonts (but could be convinced otherwise if looks great):
-- Section titles - Aleo
-- Main body - Lato
-- TeamPrismly logo - Philosopher

Things we like:
-- We like a big slider as the top of the landing page.

Colors to include:
-- Colors in the logo (red, blue, green, teal) as accent colors

Feel of the site:
-- Cutting-edge Software
-- Professional
-- Social Network flare (we analyze relationships)

Note:
If we find a great match with a designer there is strong possibility to continue the relationship with follow on work redesigning our web-based application.

Target Market(s)

Current customers are Harwell Pike & Morrow, Copperline Trust Bank.
We target anyone that manages a large team. Such as Corporate Leaders, High Level Managers, HR Leaders

Industry/Entity Type

Business Software

Contact Information for Business Card

Logo image
Name of company "TEAMPRISMLY" In Philosopher font.
Tagline: "Reveal the Quiet Strength Of Every Crew"
Person's Name, Title, email, phone.

Coding

Coded - Design and coding required

Number of Pages Required

4 page

Font styles to use
Other font styles liked:
• Lato, Philosopher, Aero

Colors
ec1f27
0255a3

Requirements
Must have
• See description.
Nice to have
• Things we like:
• We like a big slider as the top of the landing page. Ours is a little clunky and outdated but something fresh and sleek would be great.
• Colors to include:
• We would like to use the colors in the logo as accent colors in the site to give a consistent look and feel.
• Feel of the site:
• Cutting-edge Software
• Professional
• Social Network flare (we analyze relationships)

```html
<!DOCTYPE html>
<html lang="en">
<head>
<meta charset="utf-8">
<title>TeamPrismly – Home</title>
<link href="https://fonts.googleapis.com/css2?family=Aleo:wght@300;400&family=Lato:wght@400;700&display=swap" rel="stylesheet">
<style>
:root{
  --brand-blue:#0255a3;
  --brand-red:#ec1f27;
  --nav-active:#6fc3e8;
  --ink:#333;
  --muted:#555;
  --soft-bg:#f2f2f2;
  --line:#ddd;
  --white:#fff;
}
*{box-sizing:border-box;margin:0;padding:0}
html,body{width:823px;height:1200px;overflow:hidden}
body{font-family:'Lato',sans-serif;color:var(--ink);background:var(--white);position:relative}
a{color:inherit;text-decoration:none}
.section-title{font-family:'Aleo',serif;font-weight:300;font-size:19px;text-align:center}
.divider{width:28px;height:1px;background:var(--line);margin:0 auto}
.btn-outline{display:block;width:90px;height:27px;line-height:25px;text-align:center;font-size:9.5px;border:1.5px solid;margin:0 auto}

/* hero */
.hero{position:absolute;left:0;top:0;width:823px;height:394px;overflow:hidden}
.hero-photo{position:absolute;inset:0;background:linear-gradient(135deg,#6d7278 0%,#8a8680 30%,#5e5a55 60%,#3f4248 100%)}
.hero-shade{position:absolute;inset:0;background:rgba(20,25,35,.28)}
.brand{position:absolute;left:62px;top:26px;display:flex;align-items:center;gap:7px;color:var(--white)}
.brand-dot{width:26px;height:26px;border-radius:50%;background:rgba(255,255,255,.25)}
.brand-name{font-family:'Lato',sans-serif;font-weight:700;font-size:15px;line-height:1}
.main-nav{position:absolute;top:31px;left:358px;display:flex;font-size:9.5px;color:var(--white)}
.main-nav a{margin-right:24px;position:relative}
.main-nav a.active{color:var(--nav-active)}
.main-nav a.active::before{content:"";position:absolute;left:0;right:0;top:-19px;height:1.5px;background:var(--nav-active)}
.client-login{position:absolute;left:685px;top:22px;width:78px;height:27px;line-height:25px;border:1.5px solid var(--white);color:var(--white);font-size:9.5px;text-align:center}
.hero-title{position:absolute;top:174px;left:0;width:823px;text-align:center;color:var(--white);font-family:'Aleo',serif;font-weight:300;font-size:26px}
.hero .btn-outline{position:absolute;left:366px;top:214px;color:var(--white);border-color:var(--white)}
.slider-arrow{position:absolute;top:183px}
.scroll-cue{position:absolute;left:405px;top:354px}

/* what we do */
.what-we-do{position:absolute;top:394px;left:0;width:823px;height:181px;background:var(--brand-blue);color:var(--white);text-align:center}
.what-we-do .section-title{margin-top:51px}
.what-we-do p{font-size:9.5px;line-height:15.5px;width:600px;margin:9px auto 0}
.what-we-do .btn-outline{margin-top:13px;border-color:rgba(255,255,255,.55)}

/* help */
.help{position:absolute;top:575px;left:0;width:823px;height:246px;text-align:center}
.help .divider{margin-top:37px}
.help .section-title{margin-top:8px}
.help .lead{font-size:9px;color:var(--muted);margin-top:6px}
.benefit-list{position:absolute;top:110px;left:0;width:823px}
.benefit{position:absolute;width:130px;margin-left:-65px;text-align:center;font-size:8.6px;line-height:13.5px;color:var(--muted)}
.benefit svg{display:block;margin:0 auto 6px}
.help .btn-outline{position:absolute;left:366px;top:190px;color:var(--ink);border-color:#bbb}

/* contact */
.contact{position:absolute;top:821px;left:0;width:823px;height:349px;background:var(--soft-bg)}
.contact .divider{margin-top:38px}
.contact .section-title{margin-top:9px}
.contact .lead{text-align:center;font-size:9px;color:var(--muted);margin-top:6px}
.locations{position:absolute;left:61px;top:99px}
.locations h3{font-family:'Aleo',serif;font-weight:400;font-size:12.5px}
.location{position:absolute;width:140px;font-size:8.6px;line-height:14px;color:var(--muted)}
.location h4{font-family:'Aleo',serif;font-weight:400;font-size:9.5px;color:var(--brand-blue);margin-bottom:5px}
.location svg{vertical-align:-1px;margin-right:3px}
.contact-form{position:absolute;left:348px;top:101px;width:414px;height:212px;background:var(--white);border:1px solid #e6e6e6;font-size:8.5px;color:#888}
.contact-form label{position:absolute}
.field{position:absolute;border:1px solid #e2e2e2;background:var(--white)}
.submit{position:absolute;left:16px;top:175px;width:382px;height:24px;background:var(--brand-blue);color:var(--white);border:0;font:9px 'Lato',sans-serif}

/* footer */
.site-footer{position:absolute;top:1170px;left:0;width:823px;height:30px;background:var(--brand-blue);color:var(--white);font-size:9px;line-height:30px}
.site-footer .copy{position:absolute;left:61px}
.site-footer nav{position:absolute;right:58px}
.site-footer nav a{margin-left:20px}
</style>
</head>
<body>

<header class="hero">
  <div class="hero-photo" role="img" aria-label="Photo of a smiling team gathered around a laptop in a meeting"></div>
  <div class="hero-shade"></div>
  <a class="brand" href="#">
    <span class="brand-dot"></span>
    <span class="brand-name">TeamPrismly</span>
  </a>
  <nav class="main-nav">
    <a class="active" href="#">Home</a>
    <a href="#">The Hidden Value</a>
    <a href="#">Benefits</a>
    <a href="#">About us</a>
    <a href="#">Careers</a>
  </nav>
  <a class="client-login" href="#">Client Login</a>
  <h1 class="hero-title">Solve the mysteries of team behaviour</h1>
  <a class="btn-outline" href="#">Get Started</a>
  <svg class="slider-arrow" style="left:16px" width="30" height="30" viewBox="0 0 30 30"><circle cx="15" cy="15" r="13.5" fill="none" stroke="#fff" stroke-width="1.5"/><path d="M20 15H10M13.5 11.5 10 15l3.5 3.5" fill="none" stroke="#fff" stroke-width="1.2"/></svg>
  <svg class="slider-arrow" style="left:777px" width="30" height="30" viewBox="0 0 30 30"><circle cx="15" cy="15" r="13.5" fill="none" stroke="#fff" stroke-width="1.5"/><path d="M10 15h10M16.5 11.5 20 15l-3.5 3.5" fill="none" stroke="#fff" stroke-width="1.2"/></svg>
  <svg class="scroll-cue" width="12" height="17" viewBox="0 0 12 17"><rect x="1" y="1" width="10" height="15" rx="5" fill="none" stroke="#fff"/><line x1="6" y1="4" x2="6" y2="7" stroke="#fff"/></svg>
</header>

<section class="what-we-do">
  <h2 class="section-title">What We Do</h2>
  <p>TeamPrismly is the first company to offer comprehensive evaluations of Employee Relationships with powerful software tools for dynamic, real-time analysis and exploration. Their platform identifies employees playing key, yet hidden, roles in the organization...</p>
  <a class="btn-outline" href="#">Learn More</a>
</section>

<section class="help">
  <div class="divider"></div>
  <h2 class="section-title">How we can help solving your problem</h2>
  <p class="lead">We aim to solve any problem related to employees</p>
  <div class="benefit-list">
    <div class="benefit" style="left:132px;top:0">
      <svg width="26" height="22" viewBox="0 0 26 22" fill="#444"><circle cx="13" cy="5" r="4"/><circle cx="5" cy="8" r="3"/><circle cx="21" cy="8" r="3"/><path d="M6 20c0-5 3-8 7-8s7 3 7 8z"/><path d="M0 19c0-4 2-6 5-6 1 0 2 .3 2.5 1-1.5 1.5-2 3-2 5z"/><path d="M26 19c0-4-2-6-5-6-1 0-2 .3-2.5 1 1.5 1.5 2 3 2 5z"/></svg>
      We aim to solve any problem<br>related to employees</div>
    <div class="benefit" style="left:270px;top:-4px">
      <svg width="34" height="26" viewBox="0 0 34 26" fill="none" stroke="#444" stroke-width="1.3"><path d="M1 1h21v13H9l-4 4v-4H1z"/><path d="M12 9h21v12h-3v4l-4-4H12z" fill="#fff"/><circle cx="18" cy="15" r=".8" fill="#444"/><circle cx="22" cy="15" r=".8" fill="#444"/><circle cx="26" cy="15" r=".8" fill="#444"/><path d="M5 5h11M5 8h6"/></svg>
      Build Better Communications<br>Pathways</div>
    <div class="benefit" style="left:412px;top:-6px">
      <svg width="28" height="28" viewBox="0 0 28 28" fill="none" stroke="#444" stroke-width="1.2"><circle cx="14" cy="11" r="10"/><circle cx="14" cy="11" r="5"/><path d="M14 8v6M4 21l-2 5M24 21l2 5M10 22l-1 4M18 22l1 4M14 21v5"/></svg>
      Encourage Innovation and<br>Positive Change</div>
    <div class="benefit" style="left:552px;top:0">
      <svg width="36" height="22" viewBox="0 0 36 22" fill="var(--brand-blue)"><circle cx="5" cy="4" r="3"/><circle cx="18" cy="3" r="3"/><circle cx="31" cy="4" r="3"/><rect x="1" y="8" width="8" height="8"/><rect x="14" y="7" width="8" height="9"/><rect x="27" y="8" width="8" height="8"/><rect x="0" y="15" width="36" height="3"/><rect x="3" y="18" width="2" height="4"/><rect x="31" y="18" width="2" height="4"/></svg>
      Develop and Retain Strong<br>"Company Culture"</div>
    <div class="benefit" style="left:691px;top:0">
      <svg width="20" height="20" viewBox="0 0 20 20" fill="#444"><rect x="0" y="13" width="3" height="7"/><rect x="5" y="9" width="3" height="11"/><rect x="10" y="5" width="3" height="15"/><rect x="15" y="0" width="3" height="20"/></svg>
      Create Stronger, More<br>Productive Teams</div>
  </div>
  <a class="btn-outline" href="#">Hidden Values</a>
</section>

<section class="contact">
  <div class="divider"></div>
  <h2 class="section-title">Contact Us to get started</h2>
  <p class="lead">Contacting us to get a sales lead is the ultimate goal.</p>
  <div class="locations">
    <h3>Contact one of our four locations</h3>
    <div class="location" style="left:0;top:29px"><h4>Cincinnati, OH</h4>
      <div><svg width="6" height="6" viewBox="0 0 6 6"><path d="M1 0l1.5 1.5L1.8 2.5q1 1.8 1.8 1.8l1-.7L6 5 5 6Q0 5 0 1z" fill="#555"/></svg>555-0142</div>
      <div><svg width="6" height="5" viewBox="0 0 6 5"><rect width="6" height="5" fill="#555"/></svg>cincinnati@teamprismly.com</div></div>
    <div class="location" style="left:143px;top:29px"><h4>Denver, CO</h4>
      <div><svg width="6" height="6" viewBox="0 0 6 6"><path d="M1 0l1.5 1.5L1.8 2.5q1 1.8 1.8 1.8l1-.7L6 5 5 6Q0 5 0 1z" fill="#555"/></svg>555-0187</div>
      <div><svg width="6" height="5" viewBox="0 0 6 5"><rect width="6" height="5" fill="#555"/></svg>denver@teamprismly.com</div></div>
    <div class="location" style="left:0;top:90px"><h4>Birmingham, AL</h4>
      <div><svg width="6" height="6" viewBox="0 0 6 6"><path d="M1 0l1.5 1.5L1.8 2.5q1 1.8 1.8 1.8l1-.7L6 5 5 6Q0 5 0 1z" fill="#555"/></svg>555-0163</div>
      <div><svg width="6" height="5" viewBox="0 0 6 5"><rect width="6" height="5" fill="#555"/></svg>birmingham@teamprismly.com</div></div>
    <div class="location" style="left:143px;top:90px"><h4>Chicago, IL</h4>
      <div><svg width="6" height="6" viewBox="0 0 6 6"><path d="M1 0l1.5 1.5L1.8 2.5q1 1.8 1.8 1.8l1-.7L6 5 5 6Q0 5 0 1z" fill="#555"/></svg>555-0187</div>
      <div><svg width="6" height="5" viewBox="0 0 6 5"><rect width="6" height="5" fill="#555"/></svg>chicago@teamprismly.com</div></div>
  </div>
  <form class="contact-form">
    <label style="left:16px;top:13px">Name:</label>
    <label style="left:211px;top:13px">Email:</label>
    <div class="field" style="left:16px;top:28px;width:186px;height:25px"></div>
    <div class="field" style="left:211px;top:28px;width:187px;height:25px"></div>
    <label style="left:16px;top:62px">Message:</label>
    <div class="field" style="left:16px;top:77px;width:382px;height:83px"></div>
    <button class="submit" type="button">Submit Message</button>
  </form>
</section>

<footer class="site-footer">
  <span class="copy">© 2016 TeamPrismly. All Rights Reserved.</span>
  <nav><a href="#">Home</a><a href="#">The Hidden Value</a><a href="#">About Us</a></nav>
</footer>

</body>
</html>
```